Product Label Design

Need a product design for our Epsom salt product, needs to have a luxurious simple feel to it. The picture attached is our brand and wordage on it, the bag we think should be a stand up bag that should be offwhite/creme color. The other picture are products that we like. We updated the packaging to be a Kraft tube box, please see the attached photo for dimensions.

```html
<!DOCTYPE html>
<html lang="en">
<head>
<meta charset="UTF-8">
<title>Bath Salt Pouch Label</title>
<link href="https://fonts.googleapis.com/css2?family=Montserrat:wght@400&display=swap" rel="stylesheet">
<style>
  :root {
    --backdrop: #b0afb0;
    --label-cream: #fdfbf7;
    --tab-black: #000000;
    --tab-text: #fdfbf6;
    --ink: #1f1f1f;
    --rule: #a8a5a3;
  }
  * { margin: 0; padding: 0; box-sizing: border-box; }
  html, body {
    width: 1200px;
    height: 2518px;
    overflow: hidden;
    background: var(--backdrop);
  }
  .label {
    position: absolute;
    left: 119px;
    top: 630px;
    width: 962px;
    height: 1258px;
    background: var(--label-cream);
    box-shadow: 2px 3px 4px rgba(0, 0, 0, 0.25);
  }
  .brand-tab {
    position: absolute;
    left: 270px;
    top: 0;
    width: 420px;
    height: 328px;
    background: var(--tab-black);
    border-radius: 0 0 12px 12px;
  }
  .brand-name {
    position: absolute;
    left: 0;
    right: 0;
    top: 187px;
    text-align: center;
    font-family: "Montserrat", sans-serif;
    font-weight: 400;
    font-size: 92px;
    line-height: 1;
    letter-spacing: 0;
    color: var(--tab-text);
    white-space: nowrap;
  }
  .contents {
    position: absolute;
    left: 261px;
    top: 638px;
    width: 440px;
    list-style: none;
    font-family: "Montserrat", sans-serif;
    font-size: 30px;
    color: var(--ink);
    text-align: center;
  }
  .contents li {
    height: 51px;
    line-height: 51px;
    border-bottom: 2px solid var(--rule);
    white-space: nowrap;
  }
  .contents li:last-child { border-bottom: none; }
  .net-weight {
    position: absolute;
    left: 0;
    right: 0;
    top: 1152px;
    text-align: center;
    font-family: "Montserrat", sans-serif;
    font-size: 28px;
    color: var(--ink);
  }
</style>
</head>
<body>
  <main class="label">
    <div class="brand-tab">
      <h1 class="brand-name">HALEN</h1>
    </div>
    <ul class="contents">
      <li>US Sourced Pure Epsom Salt</li>
      <li>(Magnesium Sulfate)</li>
      <li>+ Abies sibirica</li>
      <li>Fir Balsam</li>
    </ul>
    <p class="net-weight">NET WT. 3LBS (1360g)</p>
  </main>
</body>
</html>
```